In house, web site post, social media post, and email blast specials/promo flyer

We are looking to update our monthly specials flyer to be sent out via Bright Mailway as well as printed and handed out in office and social media and posted to our website. Please see attachments below for a sample of a previous flyer. We want it to look clean and not too busy. It should be professional looking as this is going to a higher end client that is paying cash for our services

Target Market(s)

Women and Men 35-55

Contact Information for Business Card

I am tired of our current business card and want a fresh updated look. We want something simple, clean, and modern looking.

Font styles to use
Sans Serif
Script

Colors
3377b5
34a7d8
85cae6
85abd2
cedeed
ecf7fb
eaf1f7

Requirements
Must have
• Clean lines, Sexy, appealing to the medical spa beauty industry. Our clients come to us to look and feel good.
• Content of actual specials:
• FIGHT FINE LINES AND WRINKLES-Purchase a minimum of 30 units of Lumivex and receive a complimentary Glycolic Acid Peel ($150 VALUE)
• THE SWEAT STOPS HERE-Permanently stop underarm sweat with DuraCalm treatments, starting at $1,950
• BRIGHTEN & TONE-IPL $ Beam Serenity package $3,500
• REDUCE FACE & LEG VEINS- 15% off packages
• VOLUMERA: CHEEKS & NL FOLDS-SECOND SYRINGE 25% OFF, THIRD SYRINGE $50 OFF
• BODY SCULPTING FOR ABDOMEN AND THIGHS-Blast unwanted fat with a trio of treatments! $4,799
Nice to have
• Here are some sample flyers of what we would like ours to look like
• https://www.kelomirskinspa.com/specials/
• https://brevanolaclinic.com/november-specials-2017/

```html
<!DOCTYPE html>
<html lang="en">
<head>
<meta charset="utf-8">
<title>Lumora Monthly Specials</title>
<link rel="stylesheet" href="https://fonts.googleapis.com/css2?family=Lato:wght@400;700;900&display=swap">
<style>
  :root {
    --backdrop: #3a3a3c;
    --paper: #ffffff;
    --teal: #3f8c8d;
    --teal-deep: #2f7476;
    --teal-band: #4a8b8d;
    --ink: #2b2b2b;
    --brand: #2f6a6c;
  }
  * { box-sizing: border-box; margin: 0; padding: 0; }
  html, body { width: 945px; height: 1200px; overflow: hidden; background: var(--backdrop); }
  body { position: relative; font-family: "Lato", sans-serif; color: var(--ink); }

  .flyer {
    position: absolute; left: 114px; top: 94px; width: 717px; height: 1013px;
    background: var(--paper); overflow: hidden;
  }
  .hero-photo {
    position: absolute; left: 0; top: 0; width: 717px; height: 400px;
    background:
      radial-gradient(ellipse 200px 160px at 540px 300px, rgba(240,230,90,.9), rgba(240,230,90,0) 70%),
      radial-gradient(ellipse 260px 200px at 560px 90px, rgba(235,130,30,.95), rgba(235,130,30,0) 75%),
      radial-gradient(ellipse 180px 240px at 240px 200px, rgba(225,185,150,.85), rgba(225,185,150,0) 70%),
      linear-gradient(90deg, #3b3a2c 0%, #6d6a3f 30%, #c58a3c 60%, #e9a540 80%, #d8c859 100%);
  }
  .wave { position: absolute; left: 0; top: 330px; width: 717px; height: 90px; }

  .brand-name {
    position: absolute; left: 462px; top: 180px;
    font-weight: 700; font-size: 40px; letter-spacing: 1px; color: var(--brand); line-height: 1;
  }

  .headline {
    position: absolute; left: 0; top: 436px; width: 717px; text-align: center;
    font-weight: 900; font-size: 34.5px; line-height: 37px; color: var(--teal); letter-spacing: -.2px;
  }

  .special { position: absolute; width: 320px; font-size: 14.5px; line-height: 18.6px; }
  .special-title { font-weight: 900; font-size: 15px; color: var(--teal); display: block; }
  .special-title.inline { display: inline; }
  .col-left { left: 60px; }
  .col-right { left: 401px; }

  .footer-band {
    position: absolute; left: 0; top: 893px; width: 717px; height: 120px; background: var(--teal-band);
  }
  .site-tab {
    position: absolute; left: 218px; top: 868px; width: 282px; height: 44px;
    background: var(--paper); border-radius: 0 0 14px 14px;
    text-align: center; font-weight: 700; font-size: 19px; line-height: 44px; color: var(--teal);
  }
  .footer-text {
    position: absolute; left: 0; top: 928px; width: 717px; text-align: center;
    color: #ffffff; font-size: 13px; line-height: 19px;
  }
  .footer-links { font-weight: 700; margin-top: 2px; }
</style>
</head>
<body>
  <main class="flyer">
    <div class="hero-photo" role="img" aria-label="Photo of a woman in a wide-brimmed dark hat with long wavy hair against a warm blurred garden background"></div>
    <svg class="wave" viewBox="0 0 717 90" preserveAspectRatio="none" aria-hidden="true">
      <path d="M0 60 C120 -10 260 40 340 50 C420 60 560 -5 717 50 L717 90 L0 90 Z" fill="#ffffff"/>
      <path d="M0 56 C120 -14 260 36 340 46 C420 56 560 -9 717 46 L717 52 C560 -3 420 62 340 52 C260 42 120 -8 0 62 Z" fill="var(--teal-deep)"/>
      <path d="M0 66 C140 20 250 62 350 70 C450 62 560 18 717 56 L717 62 C560 26 450 72 350 78 C250 72 140 28 0 72 Z" fill="var(--teal)"/>
    </svg>

    <div class="brand-name">LUMORA</div>

    <h1 class="headline">PLEASE CALL TO SCHEDULE YOUR<br>APPOINTMENT TODAY 503.555.0142</h1>

    <section class="special col-left" style="top:545px">
      <span class="special-title">FIGHT FINE LINES AND WRINKLES</span>
      Purchase a minimum of 30 units of<br>Lumivex and receive a complimentary<br>Glycolic Acid Peel<br>($150 VALUE)
    </section>
    <section class="special col-left" style="top:676px">
      <span class="special-title">BRIGHTEN &amp; TONE-IPL $</span>
      Beam Serenity package<br>$3,500
    </section>
    <section class="special col-left" style="top:761px; width:330px">
      <span class="special-title inline">VOLUMERA:</span> CHEEKS &amp; NL FOLDS-SECOND<br>SYRINGE 25% OFF, THIRD SYRINGE<br>$50 OFF
    </section>

    <section class="special col-right" style="top:545px">
      <span class="special-title">THE SWEAT STOPS HERE</span>
      Permanently stop underarm<br>sweat with DuraCalm treatments,<br>starting at<br>$1,950
    </section>
    <section class="special col-right" style="top:667px">
      <span class="special-title">REDUCE FACE &amp; LEG VEINS</span>
      15% off packages
    </section>
    <section class="special col-right" style="top:742px">
      <span class="special-title inline">BODY SCULPTING FOR ABDOMEN<br>AND THIGHS</span> Blast unwanted fat<br>with a trio of treatments!<br>$4,799
    </section>

    <div class="footer-band"></div>
    <div class="site-tab">lumoraportland.com</div>
    <footer class="footer-text">
      <p>2140 NW Alder Court, Suite 2, Portland, Oregon 97210 503.555.0142</p>
      <p>Visit lumoraportland.com for a more beautiful body, inside and out.</p>
      <p class="footer-links">www.kelomirskinspa.com/specials/ | brevanolaclinic.com/november-specials-2017/</p>
    </footer>
  </main>
</body>
</html>
```